Wexley Foot & Ankle Millbrook Window Vinyl Cling

Hi,
I'm looking to get a window decal done, but need it professionally designed.
-must be 24" x 24"
-Quorum Font
-Include our logo, Podiatry, phone number and website
- The goal is to make this eye catching.
Thank you,
Dorian

```html
<!DOCTYPE html>
<html lang="en">
<head>
<meta charset="utf-8">
<title>Wexley Foot &amp; Ankle Millbrook – Window Cling Options</title>
<link rel="stylesheet" href="https://fonts.googleapis.com/css2?family=Signika:wght@500;600&display=swap">
<style>
  :root {
    --stage: #4a4a4a;
    --paper: #ffffff;
    --teal: #57c2a6;
    --orange: #f2804a;
    --ink-light: #ffffff;
  }
  * { box-sizing: border-box; margin: 0; padding: 0; }
  html, body {
    width: 1200px; height: 1200px; overflow: hidden;
    background: var(--stage);
    font-family: "Signika", "Trebuchet MS", sans-serif;
  }
  .board { position: relative; width: 1200px; height: 1200px; }

  .cling {
    position: absolute;
    width: 510px; height: 455px;
    background: var(--paper);
  }
  .cling--a { left: 55px;  top: 114px; }
  .cling--b { left: 635px; top: 114px; }
  .cling--c { left: 55px;  top: 631px; }
  .cling--d { left: 635px; top: 631px; }

  .brand {
    position: absolute; left: 42px; top: 22px; width: 412px; height: 116px;
  }
  .brand-mark {
    position: absolute; left: 0; bottom: 6px;
    width: 56px; height: 56px;
    background: var(--teal);
  }
  .brand-text {
    position: absolute; right: 0; top: 10px;
    text-align: right; white-space: nowrap;
  }
  .brand-line {
    display: block;
    font-weight: 600; font-size: 44px; line-height: 40px;
    color: var(--orange); text-transform: uppercase; letter-spacing: 0.5px;
  }
  .brand-location {
    display: block; margin-top: 2px;
    font-weight: 600; font-size: 28px; line-height: 28px;
    color: var(--teal); text-transform: uppercase; letter-spacing: 0.5px;
  }

  .service-band {
    position: absolute; left: 20px; top: 156px; width: 470px; height: 147px;
    display: flex; flex-direction: column; align-items: center; justify-content: center;
    color: var(--ink-light); text-align: center;
  }
  .service-title { font-weight: 600; font-size: 60px; line-height: 1; }
  .service-subtitle { font-weight: 500; font-size: 40px; line-height: 1; margin-top: 8px; white-space: nowrap; }

  .phone {
    position: absolute; left: 0; top: 308px; width: 510px;
    text-align: center; font-weight: 600; font-size: 43px; line-height: 54px;
    letter-spacing: 1px;
  }

  .web-band {
    position: absolute; left: 20px; top: 366px; width: 470px; height: 65px;
    display: flex; align-items: center; justify-content: center;
    color: var(--ink-light); font-weight: 600; font-size: 36px;
  }

  .is-teal   { background: var(--teal); }
  .is-orange { background: var(--orange); }
  .text-teal   { color: var(--teal); }
  .text-orange { color: var(--orange); }
</style>
</head>
<body>
<main class="board">

  <section class="cling cling--a">
    <div class="brand">
      <span class="brand-mark"></span>
      <div class="brand-text">
        <span class="brand-line">Wexley</span>
        <span class="brand-line">Foot &amp; Ankle</span>
        <span class="brand-location">Millbrook</span>
      </div>
    </div>
    <div class="service-band is-teal">
      <span class="service-title">Podiatry</span>
      <span class="service-subtitle">Foot &amp; Ankle Physicians</span>
    </div>
    <p class="phone text-teal">(877) 555 - 0148</p>
    <div class="web-band is-teal">StepWellFeet.com</div>
  </section>

  <section class="cling cling--b">
    <div class="brand">
      <span class="brand-mark"></span>
      <div class="brand-text">
        <span class="brand-line">Wexley</span>
        <span class="brand-line">Foot &amp; Ankle</span>
        <span class="brand-location">Millbrook</span>
      </div>
    </div>
    <div class="service-band is-orange">
      <span class="service-title">Podiatry</span>
      <span class="service-subtitle">Foot &amp; Ankle Physicians</span>
    </div>
    <p class="phone text-orange">(877) 555 - 0148</p>
    <div class="web-band is-orange">StepWellFeet.com</div>
  </section>

  <section class="cling cling--c">
    <div class="brand">
      <span class="brand-mark"></span>
      <div class="brand-text">
        <span class="brand-line">Wexley</span>
        <span class="brand-line">Foot &amp; Ankle</span>
        <span class="brand-location">Millbrook</span>
      </div>
    </div>
    <div class="service-band is-teal">
      <span class="service-title">Podiatry</span>
      <span class="service-subtitle">Foot &amp; Ankle Physicians</span>
    </div>
    <p class="phone text-teal">(877) 555 - 0148</p>
    <div class="web-band is-orange">StepWellFeet.com</div>
  </section>

  <section class="cling cling--d">
    <div class="brand">
      <span class="brand-mark"></span>
      <div class="brand-text">
        <span class="brand-line">Wexley</span>
        <span class="brand-line">Foot &amp; Ankle</span>
        <span class="brand-location">Millbrook</span>
      </div>
    </div>
    <div class="service-band is-orange">
      <span class="service-title">Podiatry</span>
      <span class="service-subtitle">Foot &amp; Ankle Physicians</span>
    </div>
    <p class="phone text-teal">(877) 555 - 0148</p>
    <div class="web-band is-teal">StepWellFeet.com</div>
  </section>

</main>
</body>
</html>
```